LUMINARA VENTURES NAMECARD

Need to design a name card with an existing logo.

As we are professional corporate services provider our name card has to project a professional image.
Should be corporate, simple & professional.

Our corporate color is maroon red but not too dull.

Please refer to our website at www.luminaraventures.com.sg

Would attach our logo herewith.

Front surface of namecard details:
LUMINARA VENTURES PTE LTD
Registration No. 208711845K

Tan Wei Ling CA (Singapore)
Director

Tel +65 6481 2957
Mobile +65 9172 3086
tan@luminaraventures.com.sg
www.luminaraventures.com.sg

47 Plover Lane
#07-12 Harbourlight Plaza
Singapore 276351

Back of namecard:-
OUR CORE SERVICES
Incorporation services
Corporate Secretarial Services
Accountancy service
Goods & Services Taxation
Corporate & Personal Taxation
Financial Reporting
Payroll Administration

AFFILIATES:
BRIGHTWAVE CORPORATE SERVICES PTE LTD
PINNACLEFORMATIONSPTE LTD
LIM MANAGEMENT SERVICES PTE LTD
RW HO AND COMPANY PTE LTD
LEDGERLY ACADEMY

```html
<!DOCTYPE html>
<html lang="en">
<head>
<meta charset="utf-8">
<title>Luminara Ventures Name Card</title>
<link rel="stylesheet" href="https://fonts.googleapis.com/css2?family=Tinos:wght@400;700&display=swap">
<style>
  :root {
    --brand-red: #cf1c32;
    --card-white: #ffffff;
    --backdrop: #ecebe9;
    --rule-red: #b81a2d;
  }
  * { box-sizing: border-box; margin: 0; padding: 0; }
  html, body {
    width: 1200px; height: 900px; overflow: hidden;
    background: var(--backdrop);
    font-family: "Tinos", "Times New Roman", serif;
  }
  .canvas { position: relative; width: 1200px; height: 900px; }

  .card {
    position: absolute;
    background: var(--card-white);
    box-shadow: 0 4px 18px rgba(0,0,0,0.12);
  }

  /* Front */
  .card-front { left: 148px; top: 68px; width: 589px; height: 364px; }
  .brand-name {
    position: absolute; left: 0; right: 0; top: 0; height: 164px;
    display: flex; align-items: center; justify-content: center;
    color: var(--brand-red); font-size: 34px; font-weight: 700;
    letter-spacing: 1px; line-height: 1;
  }

  .front-band {
    position: absolute; left: 0; top: 164px; width: 100%; height: 200px;
    background: var(--brand-red); color: var(--card-white);
  }
  .person { position: absolute; left: 28px; top: 16px; }
  .person-name { font-size: 23px; font-weight: 700; line-height: 28px; }
  .person-role { font-size: 16.5px; line-height: 22px; }

  .contact-list { position: absolute; left: 28px; top: 95px; list-style: none; }
  .contact-list li {
    display: flex; align-items: center; font-size: 17px; line-height: 21.5px;
  }
  .contact-list svg { width: 13px; height: 13px; margin-right: 8px; fill: var(--card-white); flex: none; }

  .company-block { position: absolute; right: 27px; top: 55px; text-align: right; }
  .company-name { font-size: 16.5px; font-weight: 700; line-height: 22px; }
  .company-reg { font-size: 16.5px; line-height: 22px; }
  .company-reg strong { font-weight: 700; }
  .company-address { margin-top: 13px; font-size: 16.5px; line-height: 21.5px; font-style: normal; }

  /* Back */
  .card-back { left: 388px; top: 505px; width: 567px; height: 352px; color: var(--brand-red); }
  .section-title {
    position: absolute; left: 0; right: 0; text-align: center;
    font-size: 18.5px; font-weight: 400; letter-spacing: 0.2px;
  }
  .services-title { top: 32px; }
  .service-list { position: absolute; list-style: none; font-size: 18.5px; line-height: 23px; }
  .service-list li::before {
    content: ""; display: inline-block; width: 6px; height: 6px; border-radius: 50%;
    background: var(--brand-red); margin-right: 6px; vertical-align: middle;
  }
  .service-list-left { left: 34px; top: 67px; }
  .service-list-right { left: 286px; top: 69px; }
  .section-rule {
    position: absolute; left: 26px; right: 24px; top: 185px;
    height: 2px; border: 0; background: var(--rule-red);
  }
  .affiliates-title { top: 200px; }
  .affiliate-list {
    position: absolute; left: 0; right: 0; top: 231px;
    list-style: none; text-align: center; font-size: 15.5px; line-height: 20.5px;
  }
</style>
</head>
<body>
<main class="canvas">

  <section class="card card-front" aria-label="Name card front">
    <div class="brand-name">LUMINARA VENTURES</div>

    <div class="front-band">
      <div class="person">
        <h1 class="person-name">Tan Wei Ling</h1>
        <p class="person-role">CA (Singapore)</p>
        <p class="person-role">Director</p>
      </div>

      <ul class="contact-list">
        <li>
          <svg viewBox="0 0 16 16" aria-hidden="true"><path d="M1 5c0-2 3-3 7-3s7 1 7 3v1.5h-3.5V5H4.5v1.5H1zM3.5 7.5h9L14 13H2z"/></svg>
          +65 6481 2957
        </li>
        <li>
          <svg viewBox="0 0 16 16" aria-hidden="true"><path d="M4.5 0.5h7v15h-7zM6 2v10.5h4V2zM7.3 13.3h1.4v1.2H7.3z" fill-rule="evenodd"/></svg>
          +65 9172 3086
        </li>
        <li>
          <svg viewBox="0 0 16 16" aria-hidden="true"><path d="M1 3h14v10H1zM2.5 4.5 8 9l5.5-4.5v-0.2H2.5z" fill-rule="evenodd"/></svg>
          tan@luminaraventures.com.sg
        </li>
        <li>
          <svg viewBox="0 0 16 16" aria-hidden="true"><circle cx="8" cy="8" r="7"/></svg>
          www.luminaraventures.com.sg
        </li>
      </ul>

      <div class="company-block">
        <p class="company-name">LUMINARA VENTURES PTE LTD</p>
        <p class="company-reg"><strong>Registration No.</strong> 208711845K</p>
        <address class="company-address">
          47 Plover Lane<br>
          #07-12 Harbourlight Plaza<br>
          Singapore 276351
        </address>
      </div>
    </div>
  </section>

  <section class="card card-back" aria-label="Name card back">
    <h2 class="section-title services-title">OUR CORE SERVICES</h2>
    <ul class="service-list service-list-left">
      <li>Incorporation Services</li>
      <li>Corporate Secretarial Services</li>
      <li>Accountancy Service</li>
      <li>Goods &amp; Services Taxation</li>
    </ul>
    <ul class="service-list service-list-right">
      <li>Corporate &amp; Personal Taxation</li>
      <li>Financial Reporting</li>
      <li>Payroll Administration</li>
    </ul>

    <hr class="section-rule">

    <h2 class="section-title affiliates-title">AFFILIATES</h2>
    <ul class="affiliate-list">
      <li>Brightwave Corporate Services Pte Ltd</li>
      <li>Pinnacle Formations Pte Ltd</li>
      <li>Lim Management Company Pte Ltd</li>
      <li>RW Ho and Company Pte Ltd</li>
      <li>Ledgerly Academy &nbsp;| Meridian Corporate Pte Ltd</li>
    </ul>
  </section>

</main>
</body>
</html>
```